Stationary for 2-office law firm with global theme

I need stationary with contact info for two offices. I'd like the same letterhead design to work for printing on stationary and also for digital use in Word. The colors and feel should match the new logo, which is a stylized globe with and "F" in it. I'd also like envelopes with an eye-catching design.

Target Market(s)

U.S. citizens seeking dual citizenship with Italy or Ireland

Industry/Entity Type

Law

Font styles to use
Serif
Sans Serif
Other font styles liked:
• To match the logo?

Colors
0054AA
0677BA
7BADD7
CADEEF
E8F1F8

Requirements
Must have
• Clean, modern design incorporating new logo

```html
<!DOCTYPE html>
<html lang="en">
<head>
<meta charset="utf-8">
<title>Verano Law — Stationery Pack</title>
<link href="https://fonts.googleapis.com/css2?family=Montserrat:wght@500;600;700&family=PT+Serif:ital,wght@0,400;0,700;1,400&display=swap" rel="stylesheet">
<style>
  :root{
    --bg:#b1b1b1;
    --navy:#0d3c6e;
    --blue:#1a9fdc;
    --grey:#4a4a4a;
    --title-grey:#5a5a5a;
    --paper:#ffffff;
    --line:#dcdcdc;
    --faint:#ececec;
    --sans:'Montserrat', Arial, sans-serif;
    --serif:'PT Serif', Georgia, serif;
  }
  *{box-sizing:border-box;margin:0;padding:0}
  html,body{width:1200px;height:900px;overflow:hidden;background:var(--bg)}
  .canvas{position:relative;width:1200px;height:900px;background:var(--bg)}

  .pack-title{position:absolute;left:61px;top:20px;font-family:var(--serif);color:var(--navy);font-weight:700;font-size:38px;letter-spacing:.5px}
  .pack-subtitle{position:absolute;left:61px;top:62px;font-family:var(--serif);font-style:italic;color:var(--title-grey);font-size:26px;letter-spacing:.5px}

  .item{position:absolute;background:var(--paper);box-shadow:0 3px 8px rgba(0,0,0,.18)}

  .logo{display:flex;align-items:center;gap:.4em;font-family:var(--sans);font-weight:700;color:var(--navy);white-space:nowrap;line-height:1}
  .logo .mark{width:1.7em;height:1.7em;border-radius:50%;background:var(--blue);flex:none}

  .pattern{position:absolute;inset:0;background:linear-gradient(140deg,var(--grey) 0%,var(--navy) 30%,var(--blue) 55%,var(--navy) 70%,var(--grey) 100%)}
  .logo-strip{position:absolute;left:0;right:0;bottom:0;background:var(--paper);display:flex;align-items:center;padding-left:10%}

  .faint-stripes{position:absolute;left:0;bottom:0;width:80%;background:linear-gradient(90deg,var(--faint),#f6f6f6 70%,rgba(255,255,255,0))}

  .address{font-family:var(--serif);color:#333;line-height:1.35}
  .address b{color:var(--navy)}

  /* letter body */
  .letter-body{position:absolute;left:25px;top:84px;width:152px;font-family:var(--sans);font-weight:600;font-size:4.3px;line-height:1.75;text-transform:uppercase;color:#222}
  .letter-body p{margin-bottom:6px}

  /* envelopes */
  .flap{position:absolute;left:0;right:0;top:0}
  .flap-navy{background:var(--navy);border-radius:10px 10px 0 0}
  .flap-blue{background:var(--blue);clip-path:polygon(0 0,100% 0,95% 100%,5% 100%);border-radius:0 0 8px 8px}

  /* calendar */
  .rings{position:absolute;left:6px;right:6px;top:-7px;height:10px;background:repeating-linear-gradient(90deg,#777 0 1.5px,transparent 1.5px 8px)}
  .cal-year{position:absolute;left:6px;right:6px;top:35px;height:8px;background:var(--navy);color:#fff;font:700 7px/8px var(--sans);text-align:center}
  .cal-grid{position:absolute;left:6px;right:6px;top:46px;display:grid;grid-template-columns:repeat(3,1fr);gap:3px 3px}
  .month{height:34px;background:#f3f3f3}
  .month h4{background:var(--navy);color:#fff;font:600 3.6px/4.5px var(--sans);text-align:center}
  .month p{font:500 3.8px/1.6 var(--sans);color:#333;padding-left:6px;word-spacing:2px}
  .cal-foot{position:absolute;left:0;right:0;bottom:4px;text-align:center;font-size:3.4px}

  /* business cards */
  .card{display:flex;flex-direction:column;align-items:center;justify-content:center;border-left:3px solid var(--navy);border-right:3px solid var(--navy);background:#efefef}
  .card-back{display:grid;grid-template-columns:1fr 1fr;gap:3px;padding:4px 6px;font-family:var(--sans);font-size:2.8px;color:#333;line-height:1.5}
  .card-back .logo{grid-column:1/3;justify-self:center;font-size:4px}

  .disc{border-radius:50%;display:flex;align-items:flex-start;justify-content:center;padding-top:22px}
  .disc .hub{position:absolute;left:50%;top:50%;width:26px;height:26px;margin:-13px 0 0 -13px;border-radius:50%;border:6px solid #d9d9d9;background:var(--bg)}

  .badge-name{position:absolute;left:52px;top:27px;font-family:var(--serif);font-size:6.5px;color:var(--navy);line-height:1.2}
  .badge-name b{font-weight:700}
</style>
</head>
<body>
<div class="canvas">

  <h1 class="pack-title">VERANO LAW</h1>
  <p class="pack-subtitle">STATIONERY PACK</p>

  <!-- Notebook -->
  <div class="item notebook" style="left:65px;top:236px;width:177px;height:220px;overflow:hidden">
    <div class="pattern" role="img" aria-label="Diagonal stripe pattern in navy, bright blue and grey"></div>
    <div class="logo-strip" style="height:40px;clip-path:polygon(0 0,60% 0,75% 100%,0 100%)">
      <div class="logo" style="font-size:10px"><span class="mark"></span>VERANO LAW</div>
    </div>
  </div>

  <!-- Letterhead with text -->
  <div class="item letterhead" style="left:301px;top:228px;width:200px;height:283px;overflow:hidden">
    <div class="logo" style="position:absolute;left:12px;top:10px;font-size:8.5px"><span class="mark"></span>VERANO LAW</div>
    <div class="letter-body">
      <p>Lorem ipsum dolor sit amet</p>
      <p>Lorem ipsum dolor sit amet reprehenderit est sanctus. Sed incididunt adipscing et diam est aute volpuptate magna justo. Lorem ipsum dolor sit amet reprehenderit est sanctus. Sed incididunt adipscing et diam est aute volpuptate magna justo. Lorem ipsum dolor sit amet et reprehenderit est sanctus.</p>
      <p>Lorem ipsum dolor sit amet reprehenderit sed incididunt adipscing et diam est aute volpuptate magna justo lorem ipsum dolor sit amet reprehenderit est sanctus.</p>
      <p>Volpuptate magna justo. Lorem ipsum dolor sit amet et reprehenderit est sanctus.</p>
    </div>
    <div class="faint-stripes" style="height:36px" role="img" aria-label="Faint diagonal stripe band"></div>
    <div class="address" style="position:absolute;left:16px;top:243px;font-size:3.6px">
      <b>Verano Law PLLC</b><br>48 Harbor Ave. Ste. 210, NYC, NY 10014<br>Email: hello@veranolaw.com<br>Tel: (212) 555-0148
    </div>
  </div>

  <!-- Folder cover -->
  <div class="item folder" style="left:540px;top:228px;width:211px;height:298px;overflow:hidden">
    <div class="pattern" role="img" aria-label="Diagonal stripe pattern in navy, bright blue and grey"></div>
    <div class="logo-strip" style="height:50px;clip-path:polygon(0 0,62% 0,75% 100%,0 100%)">
      <div class="logo" style="font-size:12px"><span class="mark"></span>VERANO LAW</div>
    </div>
  </div>

  <!-- Calendar -->
  <div class="item calendar" style="left:786px;top:234px;width:168px;height:208px">
    <div class="rings"></div>
    <div class="logo" style="position:absolute;left:56px;top:14px;font-size:7px"><span class="mark"></span>VERANO LAW</div>
    <div class="cal-year">2023</div>
    <div class="cal-grid">
      <div class="month"><h4>JANUARY</h4><p>2 9 16 23 30</p><p>4 11 18 25</p><p>6 13 20 27</p></div>
      <div class="month"><h4>FEBRUARY</h4><p>1 8 15 22</p><p>3 10 17 24</p><p>5 12 19 26</p></div>
      <div class="month"><h4>MARCH</h4><p>1 8 15 22 29</p><p>3 10 17 24</p><p>5 12 19 26</p></div>
      <div class="month"><h4>APRIL</h4><p>3 10 17 24</p><p>5 12 19 26</p><p>7 14 21 28</p></div>
      <div class="month"><h4>MAY</h4><p>1 8 15 22 29</p><p>3 10 17 24</p><p>5 12 19 26</p></div>
      <div class="month"><h4>JUNE</h4><p>2 9 16 23 30</p><p>4 11 18 25</p><p>6 13 20 27</p></div>
      <div class="month"><h4>JULY</h4><p>3 10 17 24</p><p>5 12 19 26</p><p>7 14 21 28</p></div>
      <div class="month"><h4>AUGUST</h4><p>1 8 15 22 29</p><p>3 10 17 24</p><p>5 12 19 26</p></div>
      <div class="month"><h4>SEPTEMBER</h4><p>4 11 18 25</p><p>6 13 20 27</p><p>1 8 15 22</p></div>
      <div class="month"><h4>OCTOBER</h4><p>2 9 16 23 30</p><p>4 11 18 25</p><p>6 13 20 27</p></div>
      <div class="month"><h4>NOVEMBER</h4><p>1 8 15 22 29</p><p>3 10 17 24</p><p>5 12 19 26</p></div>
      <div class="month"><h4>DECEMBER</h4><p>4 11 18 25</p><p>6 13 20 27</p><p>1 8 15 22</p></div>
    </div>
    <div class="address cal-foot">48 Harbor Ave. Ste. 210, NYC, NY 10014<br>Email: hello@veranolaw.com<br>Tel: (212) 555-0148</div>
  </div>

  <!-- ID badge -->
  <div class="item badge" style="left:1008px;top:416px;width:104px;height:64px;overflow:hidden">
    <div class="logo" style="position:absolute;left:10px;top:11px;font-size:4.5px"><span class="mark"></span>VERANO LAW</div>
    <div class="badge-name"><b>FULL NAME</b><br>TITLE</div>
    <div class="faint-stripes" style="height:16px;width:45%" role="img" aria-label="Faint diagonal stripe band"></div>
  </div>

  <!-- Business cards -->
  <div class="item card" style="left:825px;top:480px;width:91px;height:45px">
    <div class="logo" style="font-size:7px"><span class="mark"></span>VERANO LAW</div>
    <div style="font:500 2.8px var(--sans);color:#555;margin-top:5px">www.veranolaw.com</div>
  </div>
  <div class="item card card-back" style="left:825px;top:537px;width:91px;height:45px">
    <div class="logo"><span class="mark"></span>VERANO LAW</div>
    <div><b>Office 01</b><br>(212) 555-0148<br>48 Harbor Ave, NYC<br>hello@veranolaw.com</div>
    <div><b>Office 02</b><br>(212) 555-0162<br>90 Vale St, NYC<br>hello@veranolaw.com</div>
  </div>

  <!-- Mug wrap -->
  <div class="item mug" style="left:1020px;top:515px;width:81px;height:106px;display:flex;align-items:center;justify-content:center">
    <div class="logo" style="font-size:7px"><span class="mark"></span>VERANO LAW</div>
  </div>

  <!-- Large envelope -->
  <div class="item envelope-large" style="left:53px;top:543px;width:211px;height:331px;overflow:hidden">
    <div class="flap flap-navy" style="height:32px"></div>
    <div class="flap flap-blue" style="top:30px;height:32px"></div>
  </div>

  <!-- Blank letterhead -->
  <div class="item letterhead" style="left:295px;top:574px;width:212px;height:299px;overflow:hidden">
    <div class="logo" style="position:absolute;left:14px;top:13px;font-size:8.5px"><span class="mark"></span>VERANO LAW</div>
    <div class="faint-stripes" style="height:36px" role="img" aria-label="Faint diagonal stripe band"></div>
    <div class="address" style="position:absolute;left:16px;top:260px;font-size:3.6px">
      <b>Verano Law PLLC</b><br>48 Harbor Ave. Ste. 210, NYC, NY 10014<br>Email: hello@veranolaw.com<br>Tel: (212) 555-0148
    </div>
  </div>

  <!-- DL envelope front -->
  <div class="item envelope-dl" style="left:537px;top:607px;width:216px;height:104px;overflow:hidden">
    <div class="logo" style="position:absolute;left:11px;top:11px;font-size:6.5px"><span class="mark"></span>VERANO LAW</div>
    <div class="address" style="position:absolute;left:147px;top:10px;font-size:3.4px">
      <b>Verano Law PLLC</b><br>48 Harbor Ave. Ste. 210, NYC, NY 10014<br>Email: hello@veranolaw.com<br>Tel: (212) 555-0148
    </div>
    <div style="position:absolute;left:112px;top:45px;width:83px;height:40px;border:1px solid var(--line);border-radius:3px;background:#f7f7f7"></div>
    <div class="faint-stripes" style="height:26px;width:60%" role="img" aria-label="Faint diagonal stripe band"></div>
  </div>

  <!-- DL envelope back -->
  <div class="item envelope-back" style="left:537px;top:742px;width:216px;height:132px;overflow:hidden">
    <div class="flap flap-navy" style="height:26px"></div>
    <div class="flap flap-blue" style="top:24px;height:27px"></div>
  </div>

  <!-- Disc -->
  <div class="item disc" style="left:813px;top:619px;width:118px;height:118px">
    <div class="logo" style="font-size:6px"><span class="mark"></span>VERANO LAW</div>
    <div class="hub"></div>
  </div>

  <!-- Disc sleeve -->
  <div class="item sleeve" style="left:810px;top:751px;width:122px;height:122px;overflow:hidden">
    <div class="pattern" role="img" aria-label="Diagonal stripe pattern in navy, bright blue and grey"></div>
    <div class="logo-strip" style="height:20px;clip-path:polygon(0 0,62% 0,75% 100%,0 100%)">
      <div class="logo" style="font-size:6px"><span class="mark"></span>VERANO LAW</div>
    </div>
  </div>

  <!-- Gift bag face -->
  <div class="item bag" style="left:967px;top:666px;width:190px;height:208px;overflow:hidden">
    <div class="pattern" role="img" aria-label="Diagonal stripe pattern in navy, bright blue and grey"></div>
    <div class="logo-strip" style="height:34px;clip-path:polygon(0 0,60% 0,72% 100%,0 100%)">
      <div class="logo" style="font-size:10px"><span class="mark"></span>VERANO LAW</div>
    </div>
  </div>

</div>
</body>
</html>
```